Business Book - Quiet Mornings at the Ledger Desk (Finding Calm Among Daily Numbers)

I'm looking for a cover that appeals to successful business people who are used to reading business titles.

The cover should feel familiar and fit in with the existing canon of bestselling business books with a vibrant, but professional look (see attached).

I want my book to stand out, but not to be frivolous. Abstract is probably best. Or close to it.

Please feel free to use my brand colours, or go with something else -

Teal
HEX #199BAB
25 / 155 / 171

Coral
HEX #EE786E
238 / 120/ 110

I don't want to include anything connected with robots or gendered assistants/business people. Or headsets.

It's only 24 hours which is mental

```html
<!DOCTYPE html>
<html lang="en">
<head>
<meta charset="UTF-8">
<title>Quiet Mornings at the Ledger Desk — Book Cover</title>
<link href="https://fonts.googleapis.com/css2?family=Bebas+Neue&family=Exo+2:wght@300;400&display=swap" rel="stylesheet">
<style>
  :root {
    --backdrop: #454545;
    --paper: #ffffff;
    --ink: #0a0a0a;
    --coral: #ee786e;
    --navy: #0f3d5c;
    --art-light: #e4ecf4;
    --art-mid: #b9cde0;
    --art-dark: #163a55;
  }
  * { margin: 0; padding: 0; box-sizing: border-box; }
  html, body {
    width: 1200px;
    height: 1077px;
    overflow: hidden;
    background: var(--backdrop);
  }
  .cover {
    position: absolute;
    left: 280px;
    top: 60px;
    width: 639px;
    height: 957px;
    background: var(--paper);
    overflow: hidden;
  }
  .cover-type {
    position: absolute;
    left: 0;
    top: 0;
    width: 639px;
    height: 957px;
  }
  .title-light {
    font-family: "Exo 2", sans-serif;
    font-weight: 300;
    font-size: 76px;
    fill: var(--ink);
  }
  .title-bold {
    font-family: "Bebas Neue", sans-serif;
    fill: var(--coral);
  }
  .title-bold--md { font-size: 140px; }
  .title-bold--lg { font-size: 190px; }
  .title-bold--sm { font-size: 150px; }
  .subtitle {
    font-family: "Exo 2", sans-serif;
    font-weight: 400;
    font-size: 28px;
    letter-spacing: 3px;
    fill: var(--navy);
  }
  .cover-art {
    position: absolute;
    left: 283px;
    top: 736px;
    width: 267px;
    height: 221px;
    background: linear-gradient(150deg, var(--art-light) 0%, var(--art-mid) 60%, var(--art-dark) 100%);
    border-radius: 110px 110px 0 40px;
    opacity: 0.85;
  }
</style>
</head>
<body>
  <main class="cover">
    <svg class="cover-type" viewBox="0 0 639 957" role="group" aria-label="Quiet Mornings at the Ledger Desk: Finding Calm Among Daily Numbers">
      <text class="title-light" x="319.5" y="134" text-anchor="middle">QUIET</text>
      <text class="title-bold title-bold--md" x="319.5" y="244" text-anchor="middle">MORNINGS</text>
      <text class="title-light" x="319.5" y="321" text-anchor="middle">AT THE</text>
      <text class="title-bold title-bold--lg" x="319.5" y="469" text-anchor="middle">LEDGER</text>
      <text class="title-bold title-bold--sm" x="319.5" y="590" text-anchor="middle">DESK</text>
      <text class="subtitle" x="319.5" y="655" text-anchor="middle">FINDING CALM AMONG</text>
      <text class="subtitle" x="319.5" y="687" text-anchor="middle">DAILY NUMBERS</text>
    </svg>
    <div class="cover-art" role="img" aria-label="Abstract illustration area in soft blue, white and navy tones"></div>
  </main>
</body>
</html>
```